Birchwood Lodge Rentals Bill Board

7x21 bill board.

Im needing a bill board for a vacation rental company. Specializing in cabin rentals.
Here are the main points I want mentioned on the billboard:

Quality vacation rentals

Accepting new vacation rental homes.

Family owned and operated.

Fernridgestays.com
865-417-3082

Use either logo whichever looks best. Be creative

Target Market(s)

Cabin owners

Industry/Entity Type

Hospitality

Font styles to use
Sans Serif

Requirements
Must have
• Would like the cabin picture to be the background. Must have the fernridge logo, phone number and website

```html
<!DOCTYPE html>
<html lang="en">
<head>
<meta charset="utf-8">
<title>Birchwood Lodge Rentals Billboard</title>
<link rel="stylesheet" href="https://fonts.googleapis.com/css2?family=Fredoka:wght@600&family=Josefin+Sans:wght@400;600&display=swap">
<style>
  :root {
    --page-bg: #e6e8ea;
    --board-bg: #f2f2f1;
    --brand-green: #5f8f6e;
    --headline-maroon: #6a242b;
    --subhead-slate: #34424d;
    --tagline-olive: #4b4a26;
    --contact-ink: #2a2a2a;
    --rule: #2b2b2b;
  }
  * { box-sizing: border-box; margin: 0; padding: 0; }
  html, body { width: 1200px; height: 759px; overflow: hidden; background: var(--page-bg); }
  .billboard {
    position: absolute; left: 0; top: 180px;
    width: 1200px; height: 400px;
    background: var(--board-bg);
    display: flex;
    overflow: hidden;
  }
  .message {
    width: 706px; height: 100%;
    display: flex; flex-direction: column; align-items: center;
    padding: 42px 40px 0;
    font-family: "Josefin Sans", sans-serif;
    white-space: nowrap;
  }
  .brand-name {
    display: flex; align-items: center; gap: 12px;
    color: var(--brand-green);
    font-weight: 600; font-size: 28px; letter-spacing: 2px;
    text-transform: uppercase; line-height: 1;
  }
  .brand-mark { width: 14px; height: 14px; border-radius: 50%; background: var(--brand-green); }
  .headline {
    margin-top: 32px;
    font-family: "Fredoka", sans-serif; font-weight: 600;
    font-size: 42px; line-height: 1; color: var(--headline-maroon);
    text-transform: uppercase; letter-spacing: 0.5px;
  }
  .subhead {
    margin-top: 12px;
    font-size: 27px; font-weight: 600; line-height: 1.1; color: var(--subhead-slate);
    text-transform: uppercase;
  }
  .tagline {
    margin-top: 14px;
    font-size: 20px; font-weight: 600; line-height: 1.1; color: var(--tagline-olive);
    text-transform: uppercase;
  }
  .divider { margin-top: 18px; width: 560px; height: 2px; background: var(--rule); }
  .contact {
    margin-top: 20px;
    font-size: 19px; line-height: 1.1; color: var(--contact-ink); letter-spacing: 4px;
  }
  .cabin-photo {
    margin: 10px 10px 10px 0;
    flex: 1;
    background: linear-gradient(180deg, #7a6a9a 0%, #e58a5c 28%, #f2b352 38%, #6b4a3a 55%, #8a4a2e 70%, #5a4a3a 100%);
  }
</style>
</head>
<body>
  <div class="billboard">
    <div class="message">
      <div class="brand-name"><span class="brand-mark"></span>Birchwood Lodge Rentals</div>
      <h1 class="headline">Quality Vacation Rentals</h1>
      <p class="subhead">Accepting new vacation rental homes</p>
      <p class="tagline">Family owned and operated</p>
      <div class="divider"></div>
      <p class="contact">865-417-3082 &nbsp;Fernridgestays.com</p>
    </div>
    <div class="cabin-photo" role="img" aria-label="Photograph of a log cabin with lit wraparound decks on a wooded hillside under a sunset sky"></div>
  </div>
</body>
</html>
```